Re-brand our business and design!

We need a simple informational website (editable for in the future use)
We need our logo(we have included logo), name, who we are, and what we do displayed.

This is our current site (which is not acceptable, and only a template site): all our information is on this site, please use it forreferanceofinformation.
Www.brightlanefixers.com

Target Market(s)

Real estate brokers, and realtors,homeowners, and anyone looking for home repairs.

Industry/Entity Type

Business

Number of Pages Required

4 page

Font styles to use
Sans Serif

Requirements
Must have
• Our name, contact info, services, and our logo (which we will Email upon request)
• MUST have originality to the site.
• custom "contact us form" or request an estimate form.
Nice to have
• page for real customer testimonies.
• page for our previous work where we can upload pics of completed jobs.
Should not have
• any infringements on any copyrights or plagiarism at all.

```html
<!DOCTYPE html>
<html lang="en">
<head>
<meta charset="UTF-8">
<title>Bright Lane Fixers – Home Repair Services</title>
<link rel="stylesheet" href="https://fonts.googleapis.com/css2?family=Lato:wght@300;400;700&family=Open+Sans:wght@400;600&display=swap">
<style>
  :root {
    --red: #e10a0a;
    --red-dark: #b80606;
    --red-deep: #8a0000;
    --ink: #1d1d1d;
    --text: #8a8a8a;
    --grey-band: #ececec;
    --grey-light: #f4f4f4;
    --grey-btn: #7d7d7d;
    --white: #ffffff;
    --line: #d6d6d6;
  }
  * { box-sizing: border-box; margin: 0; padding: 0; }
  html, body { width: 1200px; height: 2835px; overflow: hidden; }
  body { position: relative; background: var(--white); font-family: "Open Sans", Arial, sans-serif; color: var(--text); }
  .abs { position: absolute; }

  /* top accent stripe */
  .accent-stripe { left: 0; top: 0; width: 1200px; height: 5px;
    background: repeating-linear-gradient(90deg, var(--red) 0 60px, #9a9a9a 60px 120px, var(--ink) 120px 180px, var(--white) 180px 200px); }

  /* header */
  .site-header { left: 0; top: 5px; width: 1200px; height: 146px; background: var(--white); }
  .brand { left: 119px; top: 48px; display: flex; align-items: center; gap: 12px; }
  .brand-mark { width: 22px; height: 22px; background: var(--red); }
  .brand-name { font-family: "Lato", sans-serif; font-weight: 700; font-size: 25px; color: var(--ink); }
  .main-nav { left: 530px; top: 37px; width: 623px; height: 66px; background: var(--red); display: flex; align-items: center; padding-left: 0; }
  .main-nav a { font-family: "Lato", sans-serif; font-size: 17px; font-style: italic; color: var(--white); text-decoration: none; height: 66px; line-height: 66px; padding: 0 21px; }
  .main-nav a.is-active { background: var(--red-dark); }

  /* hero */
  .hero { left: 0; top: 151px; width: 1200px; height: 596px; overflow: hidden; }
  .hero-photo { position: absolute; inset: 0;
    background: linear-gradient(180deg, #c9cdd2 0%, #e7e7e4 35%, #dcdad6 60%, #8a5a38 78%, #6d4226 100%); }
  .hero-copy { position: absolute; left: 0; width: 1200px; top: 140px; text-align: center; color: var(--white); }
  .hero-lead { width: 600px; margin: 0 auto; font-family: "Lato", sans-serif; font-size: 18px; line-height: 24px; opacity: .95; }
  .hero-title { display: inline-block; margin-top: 18px; padding: 10px 0 12px; border-top: 2px solid var(--white); border-bottom: 2px solid var(--white);
    font-family: "Lato", sans-serif; font-weight: 700; font-size: 60px; line-height: 64px; letter-spacing: -0.5px; }
  .hero-cta { position: absolute; left: 429px; top: 327px; width: 342px; height: 80px; background: var(--red);
    color: var(--white); font-family: "Lato", sans-serif; font-size: 27px; line-height: 80px; text-align: center; box-shadow: 0 3px 6px rgba(0,0,0,.25); }
  .hero-arrows { position: absolute; left: 553px; top: 516px; display: flex; gap: 16px; }
  .hero-arrows span { width: 38px; height: 38px; border: 2px solid var(--white); border-radius: 50%; display: flex; align-items: center; justify-content: center; }

  /* shared section headings */
  .section-title { font-family: "Lato", sans-serif; font-weight: 300; font-size: 30px; color: var(--red); line-height: 36px; }
  .section-title::before { content: ""; display: block; width: 81px; height: 2px; background: var(--red); margin-bottom: 22px; }

  /* who we are */
  .about { left: 119px; top: 790px; width: 545px; }
  .about p { font-size: 11.5px; line-height: 21px; margin-top: 16px; }
  .about p.is-strong { color: var(--ink); }
  .about .read-more { color: var(--red); }
  .about .section-title + p { margin-top: 18px; }

  .consult-card { left: 752px; top: 850px; width: 327px; height: 318px; background: #efefef; border: 6px solid #dcdcdc; padding: 14px 18px; }
  .consult-card h3 { font-family: "Lato", sans-serif; font-weight: 700; font-size: 18px; color: var(--red); margin-bottom: 18px; }
  .field { display: block; width: 100%; height: 41px; background: var(--white); border: 1px solid #bdbdbd; font-size: 10px; color: #a9a9a9; padding: 12px 14px; margin-bottom: 8px; }
  .field.is-tall { height: 90px; }
  .consult-card .submit { height: 40px; background: var(--red); color: var(--white); font-family: "Lato", sans-serif; font-weight: 700; font-size: 17px; text-align: center; line-height: 40px; margin-top: 4px; }

  /* services */
  .services-band { left: 0; top: 1223px; width: 1200px; height: 361px; background: var(--grey-band); }
  .services-title { left: 119px; top: 1262px; }
  .service-card { top: 1340px; width: 153px; height: 197px; background: var(--white); padding: 7px; }
  .service-photo { height: 98px; }
  .service-card h4 { font-family: "Open Sans", sans-serif; font-weight: 400; font-size: 10.5px; color: var(--ink); margin-top: 6px; }
  .service-card p { font-size: 9px; line-height: 12px; margin-top: 3px; color: #9a9a9a; }
  .carousel-arrow { top: 1429px; width: 22px; height: 22px; background: var(--white); display: flex; align-items: center; justify-content: center; }

  /* our work */
  .work-title { left: 119px; top: 1631px; }
  .work-item { width: 229px; }
  .work-frame { height: 166px; background: #e3e3e3; padding: 7px; }
  .work-photo { height: 152px; }
  .work-item p { font-size: 12px; color: var(--ink); margin-top: 12px; padding-left: 7px; }
  .load-more { left: 401px; top: 2185px; width: 399px; height: 57px; background: var(--grey-btn); color: var(--white);
    font-family: "Lato", sans-serif; font-size: 15px; text-align: center; line-height: 57px; box-shadow: 0 2px 4px rgba(0,0,0,.2); }

  /* connect */
  .connect { left: 0; top: 2310px; width: 1200px; height: 280px; background: var(--grey-light); }
  .connect-title { left: 119px; top: 2329px; font-size: 24px; }
  .connect-title::before { margin-bottom: 16px; }
  .connect-field { background: var(--white); border: 1px solid #d9d9d9; font-size: 9px; color: #b5b5b5; padding: 8px 10px; }
  .send-btn { left: 119px; top: 2531px; width: 81px; height: 30px; background: #111; color: var(--white); font-size: 11px; font-weight: 600; text-align: center; line-height: 30px; }
  .map { left: 567px; top: 2310px; width: 513px; height: 280px;
    background: linear-gradient(135deg, #ece7dd 0%, #e4e0d6 45%, #c9dcc0 70%, #b9cfe6 100%); }

  /* footer */
  .footer-main { left: 0; top: 2590px; width: 1200px; height: 151px; background: var(--red); }
  .footer-nav { left: 0; top: 2628px; width: 1200px; display: flex; justify-content: center; gap: 22px; }
  .footer-nav a { font-size: 12px; font-weight: 600; color: var(--white); text-decoration: none; }
  .social { left: 0; top: 2671px; width: 1200px; display: flex; justify-content: center; gap: 10px; }
  .social span { width: 32px; height: 32px; border: 2px solid var(--white); border-radius: 50%; }
  .footer-base { left: 0; top: 2741px; width: 1200px; height: 94px; background: var(--red-deep); }
  .footer-brand { left: 121px; top: 2775px; font-family: "Lato", sans-serif; font-weight: 700; font-size: 17px; color: var(--white); display: flex; align-items: center; gap: 8px; }
  .footer-brand .brand-mark { width: 14px; height: 14px; background: var(--white); }
  .footer-links { top: 2768px; list-style: none; }
  .footer-links li { font-size: 9.5px; color: var(--white); line-height: 19px; }
  .footer-links li::before { content: "•"; margin-right: 6px; }
  .copyright { left: 905px; top: 2782px; font-size: 9.5px; color: #c43a3a; }
</style>
</head>
<body>

<div class="abs accent-stripe"></div>

<header class="abs site-header">
  <div class="abs brand" style="top:43px">
    <span class="brand-mark"></span>
    <span class="brand-name">Bright Lane Fixers</span>
  </div>
  <nav class="abs main-nav">
    <a class="is-active">Home</a>
    <a>Who We Are</a>
    <a>Services</a>
    <a>About Us</a>
    <a>Contact Us</a>
  </nav>
</header>

<section class="abs hero">
  <div class="hero-photo" role="img" aria-label="Bright empty room with skylight, wooden floor and large windows"></div>
  <div class="hero-copy">
    <p class="hero-lead">Looking for someone to help get your listing ready to show? A complete Home Repair Solution? Did an inspection reveal repairs needed before closing? Bright Lane Fixers can help!</p>
    <h1 class="hero-title">HOME REPAIR SERVICES</h1>
  </div>
  <div class="hero-cta">GET FREE QUOTE</div>
  <div class="hero-arrows">
    <span><svg width="10" height="14" viewBox="0 0 10 14"><path d="M8 1 2 7l6 6" fill="none" stroke="#fff" stroke-width="2"/></svg></span>
    <span><svg width="10" height="14" viewBox="0 0 10 14"><path d="M2 1l6 6-6 6" fill="none" stroke="#fff" stroke-width="2"/></svg></span>
  </div>
</section>

<section class="abs about">
  <h2 class="section-title">Who We Are</h2>
  <p>Sed ut perspiciatis unde omnis iste natus error sit voluptatem accusantium doloremque laudantium, totam rem aperiam, eaque ipsa quae ab illo inventore veritatis et quasi architecto beatae vitae dicta rem aperiam, eaque ipsa quae ab illo inventore veritatis et quasi architecto beatae vitae dicta sunt explicabo. Nemo enim ipsam voluptatem quia voluptas sit aspernatur aut odit aut fugit,</p>
  <p class="is-strong">Neque porro quisquam est, qui dolorem ipsum quia dolor sit amet, consectetur, adipisci velit, sed quia non numquam eius modi tempora incidunt ut labore et dolore</p>
  <p>magnam aliquam quaerat voluptatem. Ut enim ad minima veniam, quis nostrum exercitationem ullam corporis suscipit reprehenderit reprehenderit qui in ea minima quaerat voluptatem. Ut enim ad minima veniam, quis nostrum exercitationem ullam corporis suscipit reprehenderit qui in ea minima veniam, quis nostrum exercitationem ullam corporis suscipit reprehenderit qui in ea voluptate velit esse quam nihil molestiae consequatur, vel illum qui dolorem eum fugiat quo voluptas nulla pariatur <span class="read-more">Read More</span></p>
</section>

<aside class="abs consult-card">
  <h3>Get Free Consultation NOW!</h3>
  <div class="field">Your Name:</div>
  <div class="field">Email Address:</div>
  <div class="field is-tall">Your Message:</div>
  <div class="submit">SUBMIT</div>
</aside>

<div class="abs services-band"></div>
<h2 class="abs section-title services-title">Services We Provide</h2>
<div class="abs carousel-arrow" style="left:119px"><svg width="8" height="10" viewBox="0 0 8 10"><path d="M6 0 0 5l6 5z" fill="#111"/></svg></div>
<div class="abs carousel-arrow" style="left:1058px"><svg width="8" height="10" viewBox="0 0 8 10"><path d="M2 0l6 5-6 5z" fill="#111"/></svg></div>

<article class="abs service-card" style="left:163px">
  <div class="service-photo" role="img" aria-label="Wooden door with lever handle" style="background:linear-gradient(90deg,#c08a4e,#8b5a2b)"></div>
  <h4>Doors &amp; Windows</h4>
  <p>Weatherstripping, Replacements<br>Glass and Screen Installation and Repair, Install locksets</p>
</article>
<article class="abs service-card" style="left:342px">
  <div class="service-photo" role="img" aria-label="Red clay roof tiles" style="background:linear-gradient(135deg,#a8594a,#7b3a30)"></div>
  <h4>Roofing Maintenance</h4>
  <p>Weatherstripping, Replacements<br>Glass and Screen Installation and Repair, Install locksets</p>
</article>
<article class="abs service-card" style="left:521px">
  <div class="service-photo" role="img" aria-label="Stacked copper pipes" style="background:linear-gradient(135deg,#c27a48,#5a2f1a)"></div>
  <h4>Plumbing</h4>
  <p>Weatherstripping, Replacements<br>Glass and Screen Installation and Repair, Install locksets</p>
</article>
<article class="abs service-card" style="left:700px">
  <div class="service-photo" role="img" aria-label="Hands working on wooden planks" style="background:linear-gradient(135deg,#d8c2a0,#a88a62)"></div>
  <h4>Carpentry</h4>
  <p>Weatherstripping, Replacements<br>Glass and Screen Installation and Repair, Install locksets</p>
</article>
<article class="abs service-card" style="left:879px">
  <div class="service-photo" role="img" aria-label="Wind turbine against blue sky" style="background:linear-gradient(160deg,#2d5fa8,#163d7a)"></div>
  <h4>Electrical</h4>
  <p>Weatherstripping, Replacements<br>Glass and Screen Installation and Repair, Install locksets</p>
</article>

<h2 class="abs section-title work-title">Our Work</h2>

<figure class="abs work-item" style="left:119px;top:1701px"><div class="work-frame"><div class="work-photo" role="img" aria-label="Finished room with shelving unit and bicycle" style="background:linear-gradient(180deg,#5a5654,#2e2b2a)"></div></div><p>Lorem ipsum dolor sit amet</p></figure>
<figure class="abs work-item" style="left:363px;top:1701px"><div class="work-frame"><div class="work-photo" role="img" aria-label="Renovated bedroom with warm lighting" style="background:linear-gradient(180deg,#b09660,#6e5230)"></div></div><p>Lorem ipsum dolor sit amet</p></figure>
<figure class="abs work-item" style="left:607px;top:1701px"><div class="work-frame"><div class="work-photo" role="img" aria-label="Finished room with shelving unit and bicycle" style="background:linear-gradient(180deg,#5a5654,#2e2b2a)"></div></div><p>Lorem ipsum dolor sit amet</p></figure>
<figure class="abs work-item" style="left:851px;top:1701px"><div class="work-frame"><div class="work-photo" role="img" aria-label="Finished room with shelving unit and bicycle" style="background:linear-gradient(180deg,#5a5654,#2e2b2a)"></div></div><p>Lorem ipsum dolor sit amet</p></figure>

<figure class="abs work-item" style="left:119px;top:1934px"><div class="work-frame"><div class="work-photo" role="img" aria-label="Finished room with shelving unit and bicycle" style="background:linear-gradient(180deg,#5a5654,#2e2b2a)"></div></div><p>Lorem ipsum dolor sit amet</p></figure>
<figure class="abs work-item" style="left:363px;top:1934px"><div class="work-frame"><div class="work-photo" role="img" aria-label="Finished room with shelving unit and bicycle" style="background:linear-gradient(180deg,#5a5654,#2e2b2a)"></div></div><p>Lorem ipsum dolor sit amet</p></figure>
<figure class="abs work-item" style="left:607px;top:1934px"><div class="work-frame"><div class="work-photo" role="img" aria-label="Finished room with shelving unit and bicycle" style="background:linear-gradient(180deg,#5a5654,#2e2b2a)"></div></div><p>Lorem ipsum dolor sit amet</p></figure>
<figure class="abs work-item" style="left:851px;top:1934px"><div class="work-frame"><div class="work-photo" role="img" aria-label="Finished room with shelving unit and bicycle" style="background:linear-gradient(180deg,#5a5654,#2e2b2a)"></div></div><p>Lorem ipsum dolor sit amet</p></figure>

<div class="abs load-more">LOAD MORE</div>

<section class="abs connect"></section>
<h2 class="abs section-title connect-title">Connect With Us</h2>
<div class="abs connect-field" style="left:119px;top:2389px;width:183px;height:31px">Name</div>
<div class="abs connect-field" style="left:312px;top:2389px;width:183px;height:31px">Email</div>
<div class="abs connect-field" style="left:119px;top:2429px;width:376px;height:91px">Message</div>
<div class="abs send-btn">SEND</div>
<div class="abs map" role="img" aria-label="Street map showing the business location with a pin"></div>

<footer>
  <div class="abs footer-main"></div>
  <nav class="abs footer-nav">
    <a>Home</a><a>Who We Are</a><a>Services</a><a>About Us</a><a>Contact Us</a>
  </nav>
  <div class="abs social" aria-label="Social media links">
    <span></span><span></span><span></span><span></span><span></span>
  </div>
  <div class="abs footer-base"></div>
  <div class="abs footer-brand"><span class="brand-mark"></span>Bright Lane Fixers</div>
  <ul class="abs footer-links" style="left:428px"><li>Products</li><li>Customer Care</li></ul>
  <ul class="abs footer-links" style="left:547px"><li>Terms &amp; Conditions</li><li>Our Blog</li></ul>
  <ul class="abs footer-links" style="left:676px"><li>Privacy Policy</li><li>Site Map</li></ul>
  <p class="abs copyright">© 2015 All Rights Reserved</p>
</footer>

</body>
</html>
```